International Supplier needs an eye catching profssional letterhead and continuation page

We need a letterhead and continuation sheet designed for a company based in Austria called VELMA Screens GmbH. We develop and install innovate glass partition wall solutions to commercial and cultural buildings and to some of the most contemporary architectural buildings in Europe. I have our inhouse design brief confirming our corporate colours, fonts and images and have our corporate logo available in a variety of formats including AI and EPS. We are open to differing design suggestions as long as they follow the colour and font specification in our corporate design brief. We are at the forefront of innovation, craftmanship and design for architectural glass, framing systems and fire rated partition systems. The final design should communicate the spirit and strength of the company.
www.velma.com / www.tarnovu.co.uk / www.brandpane.com

Target Market(s)

Architects, planners, designers, building contractors and construction companies

Industry/Entity Type

Architecture

Font styles to use
Sans Serif

Requirements
Must have
• VELMA Screens GmbH
• Lindorfergasse 4 B
• 7000 Eisenstadt
• Österreich
• Tel: +43 (1) 482 6170
• E-mail:office@velmascreens.at
• Web:www.velmascreens.at / www.velmabrandpane.com
• subtle yet professionally distinctive
• colours and fonts to be taken ffom VELMA design guide but we are also open to variations on the same theme
Should not have
• No bold lines

```html
<!DOCTYPE html>
<html lang="de">
<head>
<meta charset="utf-8">
<title>VELMA Screens GmbH – Letterhead</title>
<link href="https://fonts.googleapis.com/css2?family=Lato:wght@300;400&display=swap" rel="stylesheet">
<style>
  :root {
    --backdrop: #dcdcdc;
    --paper: #fbfbfb;
    --crimson: #c8102e;
    --crimson-soft: #cc3358;
    --ink: #1a1a1a;
    --rule: #2a2a2a;
    --drawing: #efefef;
  }
  * { box-sizing: border-box; margin: 0; padding: 0; }
  html, body {
    width: 1200px; height: 800px; overflow: hidden;
    background: var(--backdrop);
    font-family: "Lato", sans-serif;
    color: var(--ink);
  }
  .letterhead {
    position: absolute; left: 330px; top: 18px;
    width: 540px; height: 764px;
    background: var(--paper);
    box-shadow: 0 2px 10px rgba(0,0,0,.12);
    overflow: hidden;
  }
  .band { position: absolute; left: 0; width: 100%; height: 56px; }
  .band--top { top: 0; background: var(--crimson-soft); }
  .band--bottom { bottom: 0; background: var(--crimson); }

  .sheet-area {
    position: absolute; left: 158px; right: 18px; top: 74px; bottom: 74px;
    background: linear-gradient(160deg, #f2f2f2 0%, var(--drawing) 60%, #f4f4f4 100%);
  }
  .column-rule {
    position: absolute; left: 140px; top: 56px; bottom: 56px;
    width: 1px; background: var(--rule);
  }
  .sidebar {
    position: absolute;
    left: -248px; top: 312px;
    width: 636px; height: 140px;
    transform: rotate(-90deg);
    display: flex; align-items: center;
    justify-content: space-between;
    padding: 0 8px 0 14px;
    white-space: nowrap;
  }
  .contact {
    flex-shrink: 0;
    display: flex; flex-direction: column; align-items: center;
    gap: 5px;
    font-size: 8.5px; line-height: 1.35; text-align: center;
    color: var(--ink);
  }
  .contact svg { width: 14px; height: 14px; fill: none; stroke: var(--crimson); stroke-width: 1.6; }
  .contact svg .solid { fill: var(--crimson); stroke: none; }
  .brand {
    flex-shrink: 0;
    display: flex; align-items: center; gap: 10px;
  }
  .brand-square { width: 34px; height: 34px; background: var(--crimson); }
  .brand-text { display: flex; flex-direction: column; align-items: flex-end; }
  .brand-name {
    font-weight: 300; font-size: 52px; line-height: .9;
    color: var(--ink);
  }
  .brand-legal {
    font-weight: 400; font-size: 11px; color: var(--crimson);
    margin-top: 4px;
  }
</style>
</head>
<body>
  <main class="letterhead">
    <div class="band band--top"></div>
    <div class="sheet-area" role="img" aria-label="Faint technical section drawing of a glass partition frame"></div>
    <div class="column-rule"></div>

    <aside class="sidebar">
      <div class="contact">
        <svg viewBox="0 0 16 16"><path class="solid" d="M8 1a5 5 0 0 0-5 5c0 3.6 5 9 5 9s5-5.4 5-9a5 5 0 0 0-5-5zm0 7a2 2 0 1 1 0-4 2 2 0 0 1 0 4z"/></svg>
        <span>Lindorfergasse 4 B<br>7000 Eisenstadt, Österreich</span>
      </div>
      <div class="contact">
        <svg viewBox="0 0 16 16"><circle cx="8" cy="8" r="6.2"/><ellipse cx="8" cy="8" rx="2.6" ry="6.2"/><path d="M1.8 8h12.4M2.8 5h10.4M2.8 11h10.4"/></svg>
        <span>www.velmascreens.at<br>www.velmabrandpane.com</span>
      </div>
      <div class="contact">
        <svg viewBox="0 0 16 16"><rect x="1.5" y="3.5" width="13" height="9"/><path d="M1.5 3.5 8 9l6.5-5.5"/></svg>
        <span>office@velmascreens.at</span>
      </div>
      <div class="contact">
        <svg viewBox="0 0 16 16"><path class="solid" d="M4.2 1.5 6.3 4 5 5.6c.8 2 2.4 3.6 4.4 4.4L11 8.7l2.5 2.1-1.3 2.6C7.4 13.2 2.8 8.6 2.6 3.8z"/></svg>
        <span>+43 (1) 482 6170</span>
      </div>
      <div class="brand">
        <div class="brand-square"></div>
        <div class="brand-text">
          <span class="brand-name">VELMA</span>
          <span class="brand-legal">VELMA Screens GmbH</span>
        </div>
      </div>
    </aside>

    <div class="band band--bottom"></div>
  </main>
</body>
</html>
```